Loan broker seeks referral card design for real estate financing

We need a design for a referral card for people who recommend us for real estate financing. If the deal goes through, each referrer will receive €750.

Text similar to: Recommend me! For every successful real estate financing referral, you will receive €750. (Other suggestions are also welcome)

The size should be no larger than A5 format, or possibly even oblong.
The design should convey security and competence and include themes such as independent advice.

The design should also include the company logo and a photo of me. Naturally, the design should also include a link to my website: www.die-wandlinger.at, along with my phone number and email address: office@die-wandlinger.at

```html
<!DOCTYPE html>
<html lang="en">
<head>
<meta charset="utf-8">
<title>Referral Card – Wandlinger Beratung GmbH</title>
<link rel="stylesheet" href="https://fonts.googleapis.com/css2?family=Bebas+Neue&family=Montserrat:wght@700;800&family=Nunito:wght@600;700&family=Open+Sans:wght@400&display=swap">
<style>
  :root {
    --page-bg: #dcdcdc;
    --brand-blue: #1a56bd;
    --deep-blue: #163f94;
    --band-grey: #6b6b6b;
    --text-grey: #555555;
    --white: #ffffff;
    --frame-top: #5b6f9c;
    --frame-bottom: #2a2d3c;
  }
  * { margin: 0; padding: 0; box-sizing: border-box; }
  html, body { width: 857px; height: 1200px; overflow: hidden; }
  body { background: var(--page-bg); position: relative; }

  .card {
    position: absolute;
    left: 89px;
    width: 679px;
    height: 478px;
    overflow: hidden;
    box-shadow: 2px 3px 5px rgba(0,0,0,0.28);
  }
  .card--front { top: 96px; background: var(--white); }
  .card--back { top: 625px; background: var(--brand-blue); }

  /* Front: hero area */
  .hero-scene {
    position: absolute; left: 0; top: 0; width: 679px; height: 216px;
    background: linear-gradient(120deg, #122f73 0%, #1d4fb0 45%, #2a62c9 100%);
  }
  .headline {
    position: absolute; left: 24px; top: 20px; width: 360px;
    font-family: "Bebas Neue", sans-serif; font-weight: 400; font-size: 66px; line-height: 1;
    color: var(--white); letter-spacing: 0.5px; text-align: center; white-space: nowrap;
  }
  .offer {
    position: absolute; left: 24px; top: 84px; width: 360px;
    font-family: "Bebas Neue", sans-serif; font-size: 24px; line-height: 25px;
    color: var(--white); text-align: center; letter-spacing: 0.2px;
  }
  .amount {
    position: absolute; left: 24px; top: 137px; width: 360px;
    font-family: "Montserrat", sans-serif; font-weight: 800; font-size: 74px;
    line-height: 1; color: var(--white); text-align: center; letter-spacing: -2px;
  }
  .suggestion-band {
    position: absolute; left: 0; top: 216px; width: 679px; height: 38px;
    background: var(--band-grey);
  }
  .suggestion-band span {
    position: absolute; left: 23px; top: 6px; width: 360px; text-align: center;
    font-family: "Bebas Neue", sans-serif; font-size: 28px; line-height: 28px;
    color: var(--white); letter-spacing: 0.4px; white-space: nowrap;
  }
  .brand-rule {
    position: absolute; left: 0; top: 384px; width: 679px; height: 4px;
    background: var(--band-grey);
  }
  .contact-band {
    position: absolute; left: 0; top: 388px; width: 679px; height: 90px;
    background: var(--brand-blue);
  }
  .phone {
    position: absolute; left: 28px; top: 12px;
    font-family: "Montserrat", sans-serif; font-weight: 700; font-size: 33px;
    color: var(--white); letter-spacing: 0.3px; white-space: nowrap;
  }
  .web-contact {
    position: absolute; left: 27px; top: 58px; white-space: nowrap;
    font-family: "Open Sans", sans-serif; font-size: 13px; color: var(--white);
  }
  .web-contact .sep { margin: 0 6px; }

  .portrait-frame {
    position: absolute; left: 425px; top: 0; width: 254px; height: 478px;
    background: linear-gradient(180deg, var(--frame-top) 0%, #6c7390 45%, var(--frame-bottom) 100%);
  }

  /* Brand lockup */
  .lockup { position: absolute; }
  .lockup svg { position: absolute; left: 0; top: 0; overflow: visible; }
  .lockup__name, .lockup__tagline {
    position: absolute; white-space: nowrap; font-family: "Nunito", sans-serif;
  }
  .lockup__name { font-weight: 700; }
  .lockup__tagline { font-weight: 600; }

  .lockup--front { left: 32px; top: 271px; width: 360px; height: 98px; }
  .lockup--front .lockup__name { left: 114px; top: 27px; font-size: 17.5px; color: var(--brand-blue); }
  .lockup--front .lockup__tagline { left: 114px; top: 49px; font-size: 14.5px; color: var(--text-grey); }

  .lockup--back { left: 137px; top: 180px; width: 420px; height: 118px; }
  .lockup--back .lockup__name { left: 131px; top: 34px; font-size: 20.5px; color: var(--white); }
  .lockup--back .lockup__tagline { left: 131px; top: 60px; font-size: 17px; color: var(--white); }
</style>
</head>
<body>

<section class="card card--front" aria-label="Referral card front">
  <div class="hero-scene" role="img" aria-label="Blue-tinted photo of a modern house"></div>

  <h1 class="headline">Recommend me!</h1>
  <p class="offer">For every successful real estate financing<br>referral you will receive</p>
  <p class="amount">€750</p>

  <div class="suggestion-band"><span>Other suggestions are also welcome</span></div>

  <div class="lockup lockup--front">
    <svg width="120" height="98" aria-hidden="true">
      <circle cx="47" cy="49" r="46" fill="none" stroke="var(--brand-blue)" stroke-width="3"/>
      <line x1="105" y1="2" x2="105" y2="96" stroke="var(--text-grey)" stroke-width="3"/>
    </svg>
    <span class="lockup__name">Wandlinger Beratung GmbH</span>
    <span class="lockup__tagline">Finanzieren, Versichern, Vorsorgen</span>
  </div>

  <div class="brand-rule"></div>
  <div class="contact-band">
    <p class="phone">+43 660 412 5087</p>
    <p class="web-contact">office@die-wandlinger.at<span class="sep">|</span>www.die-wandlinger.at</p>
  </div>

  <div class="portrait-frame" role="img" aria-label="Portrait photo of the advisor in a dark suit and white shirt"></div>
</section>

<section class="card card--back" aria-label="Referral card back">
  <div class="lockup lockup--back">
    <svg width="130" height="118" aria-hidden="true">
      <circle cx="56" cy="58" r="54" fill="none" stroke="var(--white)" stroke-width="3.5"/>
      <line x1="122" y1="0" x2="122" y2="116" stroke="var(--white)" stroke-width="3"/>
    </svg>
    <span class="lockup__name">Wandlinger Beratung GmbH</span>
    <span class="lockup__tagline">Finanzieren, Versichern, Vorsorgen</span>
  </div>
</section>

</body>
</html>
```